Aerial Imaging and photgraphy business card

Design a business card with eye catching aerial photo of country side / landscape with a drone in the foreground.
Also contact details.

Target Market(s)

Aerial Imaging photography

Industry/Entity Type

Advertising

Contact Information for Business Card

Dorrit
0499152036
Website http://www.crestvaleoutlooks.com.au/
email address : crestvaleoutlooks.com.au

Colors
e8f1ca
cadf82
9bcb3c
33a6d7
85cae6
cee9f5

Requirements
Must have
• High res photo
• QPT drone in the foreground Either M740 and qpt Solace or both
Nice to have
• high resolution landscape country photo on the front of the card with a QPT M740 drone in the foreground.

```html
<!DOCTYPE html>
<html lang="en">
<head>
<meta charset="utf-8">
<title>Crestvale Outlooks – Business Card</title>
<link href="https://fonts.googleapis.com/css2?family=Roboto:wght@400;700&display=swap" rel="stylesheet">
<style>
  :root {
    --backdrop: #2a2a2c;
    --card-light: #d3d5d6;
    --card-mid: #bfc2c4;
    --ink-dark: #3a3d40;
    --ink-body: #4b4f52;
    --leaf: #9bcb3c;
    --leaf-soft: #cadf82;
    --sky: #cee9f5;
    --sky-mid: #85cae6;
  }
  html, body {
    margin: 0;
    width: 1200px;
    height: 800px;
    overflow: hidden;
    background: var(--backdrop);
    font-family: "Roboto", Arial, sans-serif;
  }
  .card {
    position: absolute;
    top: 245px;
    width: 540px;
    height: 309px;
    border-radius: 16px;
    overflow: hidden;
    background: linear-gradient(160deg, var(--card-light), var(--card-mid));
  }
  .card-front { left: 40px; }
  .card-back { left: 620px; display: flex; align-items: center; justify-content: center; }
  .card-art {
    position: absolute;
    inset: 0;
    width: 540px;
    height: 309px;
  }
  .brand {
    display: flex;
    align-items: center;
    font-weight: 700;
    color: var(--ink-dark);
    white-space: nowrap;
  }
  .brand-dot {
    border-radius: 50%;
    background: var(--leaf);
    flex: none;
  }
  .card-front .brand {
    position: absolute;
    left: 34px;
    top: 48px;
    gap: 8px;
    font-size: 18px;
  }
  .card-front .brand-dot { width: 14px; height: 14px; }
  .card-back .brand {
    gap: 14px;
    font-size: 32px;
  }
  .card-back .brand-dot { width: 26px; height: 26px; }
  .contact {
    position: absolute;
    left: 34px;
    top: 170px;
    color: var(--ink-body);
  }
  .contact-name {
    font-size: 16px;
    font-weight: 700;
    color: var(--ink-dark);
    margin: 0 0 8px;
  }
  .contact-line {
    display: flex;
    align-items: center;
    gap: 7px;
    font-size: 11px;
    margin: 0 0 4px;
    white-space: nowrap;
  }
  .contact-icon {
    width: 11px;
    height: 11px;
    flex: none;
  }
</style>
</head>
<body>
  <div class="card card-front">
    <svg class="card-art" viewBox="0 0 1000 572">
      <defs>
        <linearGradient id="landscape" x1="0" y1="0" x2="0" y2="1">
          <stop offset="0" stop-color="#e9eef0"/>
          <stop offset="0.22" stop-color="#b9c7bf"/>
          <stop offset="0.45" stop-color="#8fae5e"/>
          <stop offset="1" stop-color="#5f8a36"/>
        </linearGradient>
      </defs>
      <path d="M455 0 C 355 150, 375 470, 505 572" fill="none" stroke="var(--leaf)" stroke-width="14"/>
      <path class="photo-area" role="img" aria-label="Aerial photo of green countryside with a lake and a camera drone hovering in the foreground"
            d="M470 0 H1000 V572 H525 C 395 470, 375 150, 470 0 Z" fill="url(#landscape)"/>
    </svg>

    <div class="brand"><span class="brand-dot"></span>Crestvale Outlooks</div>

    <div class="contact">
      <p class="contact-name">Dorrit</p>
      <p class="contact-line">
        <svg class="contact-icon" viewBox="0 0 18 18"><rect x="4" y="1" width="10" height="16" rx="2" fill="none" stroke="var(--leaf)" stroke-width="2"/><circle cx="9" cy="14" r="1.2" fill="var(--leaf)"/></svg>
        0499152036
      </p>
      <p class="contact-line">
        <svg class="contact-icon" viewBox="0 0 18 18"><rect x="1" y="3" width="16" height="12" rx="1.5" fill="var(--leaf)"/><path d="M1.5 4 L9 10 L16.5 4" fill="none" stroke="#fff" stroke-width="1.5"/></svg>
        info@crestvaleoutlooks.com.au
      </p>
      <p class="contact-line">
        <svg class="contact-icon" viewBox="0 0 18 18"><circle cx="9" cy="9" r="8" fill="var(--leaf)"/><path d="M1 9 H17 M9 1 C5 5, 5 13, 9 17 M9 1 C13 5, 13 13, 9 17" fill="none" stroke="#fff" stroke-width="1.2"/></svg>
        www.crestvaleoutlooks.com.au
      </p>
    </div>
  </div>

  <div class="card card-back">
    <div class="brand"><span class="brand-dot"></span>Crestvale Outlooks</div>
  </div>
</body>
</html>
```